Vireo M.K. - Diagnostic Ultrasound Flyer

About US
Vireo M.K. is a concierge ultrasound company that provides onsite or offsite diagnostic ultrasounds. We have over 14 years experience in sonography, business management, and customer service. We offer both the physician and patient flexibility, convenience, and access to timely services.

We provide ultrasounds for the following specialties:
Obstetrics/Gynecology
Abdominal
Small Parts
Vascular

Company Features:
1. Onsite or Offsite Scans
2. Images Available Immediately for Referring Physician and Patient
3. Flexible Options for Ultrasound Interpretation/Billing
4. Access to Interpreting Radiologist
5. Final Report Process - 1-2 Business Days/ 1 hour for STAT.
6. PACS Storage with Secure Access.

We need a place to add in our contact information (address, email, website, phone)

We already have a logo and would like to use it ( they are attached). We would the colors to match the logo colors....maybe lighter version of yellow and blue.

```html
<!DOCTYPE html>
<html lang="en">
<head>
<meta charset="utf-8">
<title>Vireo M.K. – Diagnostic Ultrasound Flyer</title>
<link rel="stylesheet" href="https://fonts.googleapis.com/css2?family=Oswald:wght@300;400;500&family=Roboto+Condensed:wght@400&display=swap">
<style>
  :root {
    --page-bg: #e2dfdd;
    --paper: #ffffff;
    --header-blue: #4b4f9f;
    --header-blue-deep: #3c4191;
    --header-blue-light: #6a6db4;
    --navy: #262c7e;
    --yellow: #f7b526;
    --white: #ffffff;
  }
  * { box-sizing: border-box; margin: 0; padding: 0; }
  html, body {
    width: 1200px; height: 1200px; overflow: hidden;
    background: var(--page-bg);
  }
  .flyer {
    position: absolute; left: 204px; top: 40px;
    width: 792px; height: 1120px;
    background: var(--paper);
    box-shadow: 0 2px 8px rgba(0,0,0,0.06);
    font-family: "Roboto Condensed", "Arial Narrow", sans-serif;
    color: var(--navy);
  }
  .hero {
    position: absolute; left: 0; top: 0; width: 792px; height: 378px;
    background: linear-gradient(115deg, var(--header-blue-light) 0%, var(--header-blue) 45%, var(--header-blue-deep) 100%);
    color: var(--white);
  }
  .brand-name {
    position: absolute; top: 58px; left: 0; right: 0;
    display: flex; justify-content: center; align-items: center; gap: 14px;
    font-family: "Oswald", sans-serif; font-weight: 500;
    font-size: 56px; letter-spacing: 4px; color: var(--yellow);
  }
  .brand-dot { width: 18px; height: 18px; border-radius: 50%; background: var(--yellow); }
  .hero-title {
    position: absolute; top: 178px; left: 0; right: 0; text-align: center;
    font-family: "Oswald", sans-serif; font-weight: 300;
    font-size: 60px; color: var(--yellow); line-height: 1;
  }
  .hero-text {
    position: absolute; top: 252px; left: 64px; width: 672px;
    font-size: 14.5px; line-height: 1.35;
  }
  .section-title {
    position: absolute; left: 0; right: 0; text-align: center;
    font-family: "Oswald", sans-serif; font-weight: 300;
    color: var(--navy); line-height: 1.05;
  }
  .specialties-title { top: 395px; font-size: 48px; }
  .features-title { top: 708px; font-size: 58px; }
  .specialty {
    position: absolute; top: 520px; width: 128px; text-align: center;
  }
  .specialty-label {
    height: 46px; display: flex; align-items: flex-end; justify-content: center;
    font-size: 19px; letter-spacing: 1.5px; line-height: 1;
  }
  .specialty-frame {
    margin-top: 1px; width: 128px; height: 128px;
    border: 5px solid var(--navy); border-radius: 8px;
    padding: 4px; background: var(--white);
  }
  .specialty-photo { width: 100%; height: 100%; border-radius: 3px; }
  .photo-obgyn { background: linear-gradient(160deg, #d9d3cc, #8a8e96); }
  .photo-abdominal { background: linear-gradient(160deg, #e9e4e1, #a89690); }
  .photo-small-parts { background: linear-gradient(160deg, #c9cbd0, #8d8a8c); }
  .photo-vascular { background: linear-gradient(160deg, #f1ece7, #c9a08e); }
  .feature-list {
    position: absolute; top: 885px; left: 52px; list-style: none;
    font-size: 19px; line-height: 35px;
  }
  .feature-list { top: 798px; }
  .contact-bar {
    position: absolute; top: 1064px; left: 56px; right: 54px;
    display: flex; justify-content: space-between; align-items: center;
    font-size: 14px;
  }
  .contact-item { display: flex; align-items: center; gap: 8px; }
  .contact-item svg { width: 22px; height: 22px; fill: var(--yellow); }
</style>
</head>
<body>
<main class="flyer">
  <header class="hero">
    <div class="hero-backdrop" role="img" aria-label="Blue-tinted photo of an ultrasound exam in progress" style="position:absolute;inset:0;"></div>
    <div class="brand-name"><span class="brand-dot"></span>VIREO M.K.</div>
    <h1 class="hero-title">About Us:</h1>
    <p class="hero-text">Vireo M.K. is a concierge ultrasound company that provides onsite or offsite diagnostic ultrasounds. We have over 14 years experience in sonography, business management, and customer service. We offer both the physician and patient flexibility, convenience, and access to timely services.</p>
  </header>

  <h2 class="section-title specialties-title">We Provide Ultrasounds For<br>The Following Specialties:</h2>

  <div class="specialty" style="left:55px;">
    <div class="specialty-label">Obstetrics<br>Gynecology</div>
    <div class="specialty-frame"><div class="specialty-photo photo-obgyn" role="img" aria-label="Photo of a patient consultation for obstetrics and gynecology"></div></div>
  </div>
  <div class="specialty" style="left:237px;">
    <div class="specialty-label">Abdominal</div>
    <div class="specialty-frame"><div class="specialty-photo photo-abdominal" role="img" aria-label="Photo of a patient with abdominal discomfort"></div></div>
  </div>
  <div class="specialty" style="left:426px;">
    <div class="specialty-label">Small Parts</div>
    <div class="specialty-frame"><div class="specialty-photo photo-small-parts" role="img" aria-label="Photo of a patient holding their neck"></div></div>
  </div>
  <div class="specialty" style="left:608px;">
    <div class="specialty-label">Vascular</div>
    <div class="specialty-frame"><div class="specialty-photo photo-vascular" role="img" aria-label="Photo of hands resting on a pregnant belly"></div></div>
  </div>

  <h2 class="section-title features-title">Company Features:</h2>
  <ol class="feature-list">
    <li>1. Onsite or Offsite Scans</li>
    <li>2. Images Available Immediately for Referring Physician and Patient</li>
    <li>3. Flexible Options for Ultrasound Interpretation/Billing</li>
    <li>4. Access to Interpreting Radiologist</li>
    <li>5. Final Report Process - 1-2 Business Days/ 1 hour for STAT.</li>
    <li>6. PACS Storage with Secure Access.</li>
  </ol>

  <footer class="contact-bar">
    <div class="contact-item">
      <svg viewBox="0 0 24 24" aria-hidden="true"><path d="M12 2a7 7 0 0 0-7 7c0 5.2 7 13 7 13s7-7.8 7-13a7 7 0 0 0-7-7zm0 9.5A2.5 2.5 0 1 1 12 6.5a2.5 2.5 0 0 1 0 5z"/></svg>
      <span>Your Address...</span>
    </div>
    <div class="contact-item">
      <svg viewBox="0 0 24 24" aria-hidden="true"><path d="M2 5h20v14H2zm2 2v.5l8 5.5 8-5.5V7zm0 2.9V17h16V9.9l-8 5.5z"/></svg>
      <span>hello@vireomk-mail.com</span>
    </div>
    <div class="contact-item">
      <svg viewBox="0 0 24 24" aria-hidden="true"><path d="M6.6 10.8a15.1 15.1 0 0 0 6.6 6.6l2.2-2.2a1 1 0 0 1 1-.25 11.4 11.4 0 0 0 3.6.57 1 1 0 0 1 1 1V20a1 1 0 0 1-1 1A17 17 0 0 1 3 4a1 1 0 0 1 1-1h3.5a1 1 0 0 1 1 1c0 1.25.2 2.45.57 3.57a1 1 0 0 1-.25 1z"/></svg>
      <span>000 000 48307</span>
    </div>
    <div class="contact-item">
      <svg viewBox="0 0 24 24" aria-hidden="true"><path d="M12 2a10 10 0 1 0 0 20 10 10 0 0 0 0-20zm6.9 6h-2.9a15.6 15.6 0 0 0-1.4-3.6A8 8 0 0 1 18.9 8zM12 4c.8 1.2 1.5 2.5 1.9 4h-3.8c.4-1.5 1.1-2.8 1.9-4zM4.3 14a8.2 8.2 0 0 1 0-4h3.4a16 16 0 0 0 0 4zm.8 2h2.9c.3 1.3.8 2.5 1.4 3.6A8 8 0 0 1 5.1 16zM8 8H5.1a8 8 0 0 1 4.3-3.6C8.8 5.5 8.3 6.7 8 8zm4 12c-.8-1.2-1.5-2.5-1.9-4h3.8c-.4 1.5-1.1 2.8-1.9 4zm2.3-6H9.7a14.5 14.5 0 0 1 0-4h4.6a14.5 14.5 0 0 1 0 4zm.3 5.6c.6-1.1 1.1-2.3 1.4-3.6h2.9a8 8 0 0 1-4.3 3.6zm1.7-5.6a16 16 0 0 0 0-4h3.4a8.2 8.2 0 0 1 0 4z"/></svg>
      <span>www.vireomk-scan.com</span>
    </div>
  </footer>
</main>
</body>
</html>
```